Plant Based, Environmentally SAFE Chemistry Business requires corporate standards covering all facet

Brightfold Resources is a Canadian based manufacturer and distributor of proprietary chemical formulations made entirely from domestically grown ingredients. These chemicals are non-toxic, non-caustic, contain no VOC's, will readily biodegrade to their natural state within 28 days, are non-corrosive and non-flammable. They carry an enviable 0-0-0-0 hazard rating and are safe for humans, pets and the environment.
We need a corporate design which includes all forms of marketing materials including business cards, stationery, brochures, case studies, power point standards, product labels and signage.
Corporate standards will include corporate colours matching the corporate logo (Green). Designs will be strong and bold but communicate the environmentally sensitive nature of the products we market.
We have attached corporate logos as well as previous efforts to create a standard for collateral literature and case studies as examples of previous attempts which we are not happy with.
The final designs should be formatted in such a way that Brightfold staff are able to change copy, wording and photos on the body of the brochure without the need of an artist or special effort. If special software is needed to accomplish this, that will need to be specified.
For more information on the company view www.brightfoldresources.ca

Target Market(s)

Oil & Gas Industry, Marine & Aviation & Hospitality Industry

Industry/Entity Type

Chemical Product

Font styles to use
Sans Serif

Colors

Designer to choose colors to be used in the design.

Requirements
Must have
• Include standards for business card, letterhead, 1 page brochure, case studies of 3 - 5 pages, basic standard power point background, product label which can be adjusted for change of product type and volumes in container. Common theme throughout.
Nice to have
• I am open to suggestions. Looking for strong theme which denotes a solid corporation..
• Corporate logo colours are green but is not absolutely essential that the theme be only green. Can incorporate several colours if it compliments the basic logo.
Should not have
• Do not want to have a rainbow of colours or be flashy. Should look like a solid responsible corporation

```html
<!DOCTYPE html>
<html lang="en">
<head>
<meta charset="utf-8">
<title>Brightfold Resources – 12 Principles</title>
<link rel="stylesheet" href="https://fonts.googleapis.com/css2?family=Carlito:wght@400;700&family=Open+Sans:wght@400&display=swap">
<style>
  :root {
    --brand-blue: #2a7bbd;
    --brand-navy: #245b86;
    --brand-green: #3fae49;
    --band-grey: #d9dde2;
    --paper: #ffffff;
    --ink: #1a1a1a;
  }
  * { margin: 0; padding: 0; box-sizing: border-box; }
  html, body { width: 927px; height: 1200px; overflow: hidden; background: var(--paper); }
  .sheet {
    position: relative;
    width: 927px;
    height: 1200px;
    overflow: hidden;
    background: var(--paper);
    font-family: "Carlito", "Calibri", sans-serif;
    color: var(--ink);
  }
  .sheet-backdrop { position: absolute; inset: 0; width: 927px; height: 1200px; }
  .brand {
    position: absolute;
    left: 36px;
    top: 26px;
    display: flex;
    align-items: center;
    gap: 20px;
  }
  .brand-mark {
    width: 70px;
    height: 70px;
    border-radius: 50%;
    background: var(--brand-green);
  }
  .brand-name {
    font-family: "Carlito", "Calibri", sans-serif;
    font-weight: 400;
    font-size: 34px;
    line-height: 34px;
    letter-spacing: 1px;
    text-transform: uppercase;
    color: var(--paper);
  }
  .page-title {
    position: absolute;
    left: 358px;
    top: 148px;
    font-family: "Open Sans", "Carlito", sans-serif;
    font-weight: 400;
    font-size: 92px;
    line-height: 1;
    letter-spacing: -1px;
    color: #000;
  }
  .intro {
    position: absolute;
    left: 109px;
    top: 312px;
    font-size: 16.5px;
  }
  .principles {
    position: absolute;
    left: 164px;
    top: 350px;
    width: 642px;
    list-style: none;
    counter-reset: principle;
    font-size: 16.5px;
    line-height: 22.5px;
  }
  .principles li {
    counter-increment: principle;
    margin-bottom: 9.5px;
  }
  .principles li::before {
    content: counter(principle) ".";
    display: inline-block;
    width: 48px;
  }
</style>
</head>
<body>
<main class="sheet">
  <svg class="sheet-backdrop" viewBox="0 0 927 1200" aria-hidden="true">
    <rect width="927" height="1200" fill="var(--brand-blue)"/>
    <path d="M420,0 C640,36 820,60 927,96 L927,0 Z" fill="var(--brand-navy)"/>
    <path d="M0,446 C130,210 420,72 927,84 L927,1200 L0,1200 Z" fill="var(--band-grey)"/>
    <path d="M0,452 C132,222 424,86 927,96 L927,1200 L0,1200 Z" fill="var(--paper)"/>
    <path d="M0,1178 C300,1150 640,1098 927,1050 L927,1200 L0,1200 Z" fill="var(--band-grey)"/>
    <path d="M0,1192 C300,1168 640,1122 927,1076 L927,1200 L0,1200 Z" fill="var(--brand-navy)"/>
  </svg>

  <header class="brand">
    <span class="brand-mark"></span>
    <span class="brand-name">Brightfold<br>Resources</span>
  </header>

  <h1 class="page-title">12 Principles</h1>

  <p class="intro">The <strong>twelve principles of green chemistry</strong> are:</p>

  <ol class="principles">
    <li>It is better to prevent waste than to treat or clean up waste after it is formed.</li>
    <li>Synthetic methods should be designed to maximize the incorporation of all materials used in the process into the final product.</li>
    <li>Wherever practicable, synthetic methodologies should be designed to use and generate substances that possess little or no toxicity to human health and the environment.</li>
    <li>Chemical products should be designed to preserve efficacy of function while reducing toxicity.</li>
    <li>The use of auxiliary substances (e.g. solvents, separation agents, etc.) should be made unnecessary wherever possible and innocuous when used.</li>
    <li>Energy requirements should be recognized for their environmental and economic impacts and should be minimized. Synthetic methods should be conducted at ambient temperature and pressure.</li>
    <li>A raw material or feedstock should be renewable rather than depleting wherever technically and economically practicable.</li>
    <li>Reduce derivatives – Unnecessary derivatization (blocking group, protection/deprotection, temporary modification) should be avoided whenever possible.</li>
    <li>Catalytic reagents (as selective as possible) are superior to stoichiometric reagents.</li>
    <li>Chemical products should be designed so that at the end of their function they do not persist in the environment and break down into innocuous degradation products.</li>
    <li>Analytical methodologies need to be further developed to allow for real-time, in-process monitoring and control prior to the formation of hazardous substances.</li>
    <li>Substances and the form of a substance used in a chemical process should be chosen to minimize potential for chemical accidents, including releases, explosions, and fires.</li>
  </ol>
</main>
</body>
</html>
```